1page Pre-launch landing page for Machine Learning startup

We need a 1page pre-launch landing page that (1) provides information on what we are building (2) core benefits and (3) email signup . Our company, Brightwell Loom, is building a Machine Learning service that makes using Machine learning so easy, any business person without technical expertise can easily use to solve their business problems.
Target Market(s)
MBAs or business people in organizations who want to test, use and maybe deploy machine learning solutions in their busines.
Industry/Entity Type
Machine Learning
Requirements
Must have
- Newsletter signup section. Link to an alpha version of the product (for small group of people participating as alpha testers)
Nice to have
- "machine learning for the rest of us"
- "machine learning SO easy, an MBA can use"
- 'test and use Machine learning solutions without knowing data science or hiring expensive data scientists.
- "I wouldn't be seen dead using this - Data Scientst, Ph.D"

```html
<!DOCTYPE html>
<html lang="en">
<head>
<meta charset="utf-8">
<title>Brightwell Loom — Machine Learning So Easy, An MBA Can Use</title>
<link rel="stylesheet" href="https://fonts.googleapis.com/css2?family=Montserrat:wght@400;500;600;700&family=Open+Sans:wght@400;600;700&display=swap">
<style>
  :root{
    --blue:#1d8fe8;
    --blue-deep:#0a5fd8;
    --blue-light:#e9f3fc;
    --navy:#1b3d6e;
    --ink:#1c1c1c;
    --muted:#6f6f6f;
    --green:#1fcf77;
    --green-deep:#10b35e;
    --teal:#19c2a6;
    --white:#ffffff;
    --line:#e6e6e6;
  }
  *{box-sizing:border-box;margin:0;padding:0}
  html,body{width:1200px;height:4296px;overflow:hidden}
  body{font-family:"Open Sans",Arial,sans-serif;color:var(--ink);background:var(--white);position:relative}
  section,header,footer{position:relative;width:1200px;overflow:hidden}

  /* Navigation */
  .site-nav{height:63px;background:var(--white);box-shadow:0 2px 8px rgba(0,0,0,.08);z-index:5}
  .brand{position:absolute;left:149px;top:10px;display:flex;flex-direction:column;align-items:center;gap:2px}
  .brand-dot{width:24px;height:24px;border-radius:50%;border:2px solid var(--blue)}
  .brand-name{font-family:"Montserrat",sans-serif;font-weight:600;font-size:13px;color:var(--blue)}
  .nav-link{position:absolute;top:23px;font-family:"Montserrat",sans-serif;font-size:13px;color:#333}
  .nav-cta{position:absolute;left:833px;top:17px;width:150px;height:29px;border-radius:15px;background:var(--blue-deep);color:var(--white);font-family:"Montserrat",sans-serif;font-weight:600;font-size:11.5px;display:flex;align-items:center;justify-content:center}
  .nav-login{position:absolute;left:1002px;top:22px;display:flex;align-items:center;gap:5px;font-family:"Montserrat",sans-serif;font-size:13px;color:var(--blue-deep)}

  /* Hero */
  .hero{height:553px;background:linear-gradient(90deg,#dcecfb 0%,#f3f8fe 60%,#eaf3fc 100%)}
  .hero-shape{position:absolute;left:0;top:0}
  .hero-title{position:absolute;left:149px;top:130px;width:460px;font-family:"Montserrat",sans-serif;font-weight:700;font-size:28px;line-height:1.25;color:var(--white)}
  .hero-text{position:absolute;left:149px;top:213px;width:440px;font-size:13.5px;line-height:1.55;font-weight:600;color:var(--white)}
  .btn-green{position:absolute;left:149px;top:326px;width:152px;height:42px;border-radius:3px;background:var(--green);color:var(--white);font-family:"Montserrat",sans-serif;font-weight:600;font-size:14px;display:flex;align-items:center;justify-content:center}
  .hero-art{position:absolute;left:665px;top:46px;width:355px;height:435px;border-radius:48% 48% 44% 44%;background:radial-gradient(circle at 40% 45%,#3aa5f0 0%,#1d8fe8 45%,#c7e2fa 100%)}

  /* Intro */
  .intro{height:534px}
  .section-title{position:absolute;left:0;width:1200px;text-align:center;font-family:"Montserrat",sans-serif;font-weight:500;font-size:36px;color:var(--ink)}
  .intro .section-title{top:126px}
  .intro-sub{position:absolute;left:0;top:200px;width:1200px;text-align:center;font-size:17px;line-height:1.7;color:var(--muted)}
  .feature{position:absolute;top:294px;width:200px;text-align:center}
  .feature-icon{width:100px;height:100px;margin:0 auto;border-radius:50%;border:2px solid var(--blue);padding:9px}
  .feature-icon span{display:block;width:100%;height:100%;border-radius:50%;background:radial-gradient(circle,#b9d3ec 0%,#6ea9dc 100%)}
  .feature h3{margin-top:16px;font-family:"Montserrat",sans-serif;font-weight:600;font-size:14px}
  .feature p{margin-top:10px;font-size:11px;line-height:1.65;color:var(--muted)}

  /* Building */
  .building{height:912px}
  .building-title{position:absolute;left:149px;top:48px;font-family:"Montserrat",sans-serif;font-weight:500;font-size:40px;color:var(--navy)}
  .building-title em{font-style:normal;color:var(--blue)}
  .photo{position:absolute}
  .photo-lab{left:149px;top:130px;width:510px;height:341px;background:linear-gradient(135deg,#d7d2e4 0%,#8f7fa6 45%,#e8e6ee 100%)}
  .photo-laptop{left:538px;top:445px;width:513px;height:341px;background:linear-gradient(135deg,#3b4450 0%,#1d2735 45%,#4a6fa0 70%,#7a6a5a 100%)}
  .copy{position:absolute;font-size:11px;line-height:1.75;color:#555}
  .copy p+p{margin-top:14px}
  .copy-a{left:673px;top:130px;width:372px}
  .copy-b{left:149px;top:497px;width:370px}

  /* Quote */
  .quote{height:264px;background:linear-gradient(100deg,var(--green-deep) 0%,var(--green) 55%,#22d48a 100%);color:var(--white);text-align:center}
  .quote blockquote{position:absolute;top:90px;left:0;width:1200px;font-family:"Montserrat",sans-serif;font-size:34px;font-weight:400}
  .quote cite{position:absolute;top:148px;left:0;width:1200px;font-style:normal;font-size:15px}

  /* Benefits */
  .benefits{height:1606px}
  .benefits .section-title{top:80px}
  .num{position:absolute;width:36px;height:36px;border-radius:50%;background:var(--blue);color:var(--white);font-family:"Montserrat",sans-serif;font-weight:700;font-size:13px;display:flex;align-items:center;justify-content:center}
  .benefit-head{position:absolute;font-family:"Montserrat",sans-serif;font-weight:500;font-size:23px;color:var(--ink)}
  .benefit-text{position:absolute;width:260px;font-size:11px;line-height:1.7;color:var(--muted)}
  .right{text-align:right}
  .card{position:absolute;width:229px;height:258px;background:var(--white);box-shadow:0 4px 14px rgba(0,0,0,.18);display:flex;align-items:center;justify-content:center}
  .card span{display:block;width:140px;height:140px;border-radius:14px}

  /* Footer */
  .signup{height:292px;background:linear-gradient(100deg,#0a78d8 0%,#1aa3f0 60%,#1d93e8 100%);color:var(--white)}
  .footer-brand{position:absolute;left:0;top:40px;width:1200px;display:flex;flex-direction:column;align-items:center;gap:6px}
  .footer-brand .brand-dot{width:50px;height:50px;border:3px solid var(--white)}
  .footer-brand .brand-name{color:var(--white);font-size:18px}
  .signup-form{position:absolute;left:398px;top:152px;display:flex}
  .signup-input{width:347px;height:46px;background:var(--white);border:0;padding:0 20px;font-family:"Open Sans",sans-serif;font-size:11px;color:#555;display:flex;align-items:center}
  .signup-btn{width:57px;height:46px;background:var(--green);display:flex;align-items:center;justify-content:center}
  .social{position:absolute;left:481px;top:226px;display:flex;gap:8px}
  .social span{width:53px;height:29px;background:var(--teal);border-radius:2px;display:flex;align-items:center;justify-content:center}
  .social span i{width:8px;height:8px;border-radius:50%;background:var(--white);display:block}
  .legal{height:72px;text-align:center;font-size:11px;padding-top:31px;color:#222}
  .legal b{font-weight:600}
</style>
</head>
<body>

<header class="site-nav">
  <div class="brand"><span class="brand-dot"></span><span class="brand-name">Brightwell Loom</span></div>
  <span class="nav-link" style="left:421px">Home</span>
  <span class="nav-link" style="left:506px">About Us</span>
  <span class="nav-link" style="left:590px">What we are Building</span>
  <span class="nav-link" style="left:760px">Benefits</span>
  <span class="nav-cta">Request access to Alpha</span>
  <span class="nav-login">
    <svg width="13" height="14" viewBox="0 0 13 14" fill="none" stroke="#0a5fd8" stroke-width="1.6"><circle cx="6.5" cy="4" r="3"/><path d="M1 13.5c0-3 2.5-5 5.5-5s5.5 2 5.5 5"/></svg>
    Login
  </span>
</header>

<section class="hero">
  <svg class="hero-shape" width="1200" height="553" viewBox="0 0 1200 553">
    <defs>
      <linearGradient id="heroBlue" x1="0" y1="0" x2="1" y2="1">
        <stop offset="0" stop-color="#1a8ff0"/>
        <stop offset="1" stop-color="#0a5fd8"/>
      </linearGradient>
    </defs>
    <path d="M0 0 H600 C680 90 700 230 690 340 C680 440 620 510 520 520 C400 530 330 470 220 480 C120 490 60 530 0 545 Z" fill="url(#heroBlue)"/>
  </svg>
  <h1 class="hero-title">Machine Learning SO Easy,<br>An MBA Can Use</h1>
  <p class="hero-text">Suspendisse potenti. Nulla tempus neque nec neque interdum bibendum. Proin vitae justo aliquam, semper turpis nec, fermentum dui. Maecenas malesuada tempus fermentum. Ut rhoncus interdum turpis nec blandit.</p>
  <span class="btn-green">Get Started</span>
  <div class="hero-art" role="img" aria-label="Illustration of a brain drawn as a circuit with coloured nodes"></div>
</section>

<section class="intro">
  <h2 class="section-title">Machine Learning For The Rest Of Us</h2>
  <p class="intro-sub">Aliquam luctus in nunc gravida consectetur. Proin consequat turpis nec lectus.<br>Maecenas ac mi non lectus pharetra euismod.</p>
  <div class="feature" style="left:287px">
    <div class="feature-icon"><span role="img" aria-label="Brain icon for deep learning"></span></div>
    <h3>Deep Learning</h3>
    <p>Fusce leo lacus, condimentum eget blandit sed, porta nec massa. Nunc ultricies commodo lacus nec lobortis.</p>
  </div>
  <div class="feature" style="left:501px">
    <div class="feature-icon"><span role="img" aria-label="Brain icon for algorithm"></span></div>
    <h3>Algorithm</h3>
    <p>Fusce leo lacus, condimentum eget blandit sed, porta nec massa. Nunc ultricies commodo lacus nec lobortis.</p>
  </div>
  <div class="feature" style="left:716px">
    <div class="feature-icon"><span role="img" aria-label="Brain icon for neural networks"></span></div>
    <h3>Neural Networks</h3>
    <p>Fusce leo lacus, condimentum eget blandit sed, porta nec massa. Nunc ultricies commodo lacus nec lobortis.</p>
  </div>
</section>

<section class="building">
  <h2 class="building-title">What We <em>Are Building?</em></h2>
  <div class="photo photo-lab" role="img" aria-label="Photo of a modern operating room with medical equipment"></div>
  <div class="copy copy-a">
    <p>Aliquam in aliquam nunc, vestibulum facilisis dolor. Integer quis sem faucibus, consectetur orci sed, blandit massa. Mauris volutpat pulvinar lobortis. Donec quis sapien a sem elementum tristique sit amet eget lectus. Sed et ex sit amet ipsum fringilla facilisis vitae vel velit. Morbi a magna euismod, mattis ipsum vitae, euismod leo. Praesent iaculis nunc et faucibus consequat. Phasellus nibh ipsum, ultricies sed eu eget, ullamcorper ultricies felis. Ut sed nibh a nibh convallis placerat pellentesque nec sapien.</p>
    <p>Integer neque est, posuere nec auctor at, placerat eget turpis. Ut in mauris non orci sodales scelerisque. Integer ac blandit ipsum. Etiam sit amet accumsan orci. Nec tibulum ultricies rutrum mauris at porta. Duis id tincidunt massa. Etiam non nisl ac purus egestas ultrices. Duis fringilla nibh dolor, non porttitor nunc imperdiet et. Proin id mollis enim, sed efficitur justo.</p>
  </div>
  <div class="copy copy-b">
    <p>Aliquam in aliquam nunc, vestibulum facilisis dolor. Integer quis sem faucibus, consectetur orci sed, blandit massa. Mauris volutpat pulvinar lobortis. Donec quis sapien a sem elementum tristique sit amet eget lectus. Sed et ex sit amet ipsum fringilla facilisis vitae vel velit. Morbi a magna euismod, mattis ipsum vitae, euismod leo. Praesent iaculis nunc et faucibus consequat. Phasellus nibh ipsum, ultricies sed eu eget, ullamcorper ultricies felis. Ut sed nibh a nibh convallis placerat pellentesque nec sapien.</p>
    <p>Integer neque est, posuere nec auctor at, placerat eget turpis. Ut in mauris non orci sodales scelerisque. Integer ac blandit ipsum. Etiam sit amet accumsan orci. Vestibulum ultricies rutrum mauris at porta. Duis id tincidunt massa. Etiam non nisl ac purus egestas ultrices. Duis fringilla nibh dolor, non porttitor nunc imperdiet et. Proin id mollis enim, sed efficitur justo.</p>
  </div>
  <div class="photo photo-laptop" role="img" aria-label="Photo of a laptop showing code on a desk beside a coffee mug"></div>
</section>

<section class="quote">
  <blockquote>“I wouldn't be seen dead using this”</blockquote>
  <cite>-Data Scientst, Ph.D</cite>
</section>

<section class="benefits">
  <h2 class="section-title">Core Benefits</h2>

  <span class="num" style="left:598px;top:211px">1.</span>
  <h3 class="benefit-head right" style="left:330px;top:271px;width:300px">Praesent Iaculis Nunc</h3>
  <p class="benefit-text right" style="left:370px;top:310px">Duis fringilla nibh dolor, non porttitor nunc imperdiet et. Proin id mollis enim, sed efficitur justo.</p>
  <div class="card" style="left:710px;top:200px"><span role="img" aria-label="Illustration of a brain on a circuit chip" style="background:radial-gradient(circle,#26c6a8 0%,#8fe0d0 60%,#ffffff 100%)"></span></div>

  <div class="card" style="left:347px;top:552px"><span role="img" aria-label="Illustration of a connected network of nodes" style="background:radial-gradient(circle,#d96b8f 0%,#6fb7e0 50%,#ffffff 100%)"></span></div>
  <span class="num" style="left:647px;top:563px">2.</span>
  <h3 class="benefit-head" style="left:647px;top:624px">Praesent Iaculis Nunc</h3>
  <p class="benefit-text" style="left:647px;top:663px">Duis fringilla nibh dolor, non porttitor nunc imperdiet et. Proin id mollis enim, sed efficitur justo.</p>

  <span class="num" style="left:598px;top:915px">3.</span>
  <h3 class="benefit-head right" style="left:330px;top:976px;width:300px">Praesent Iaculis Nunc</h3>
  <p class="benefit-text right" style="left:370px;top:1015px">Duis fringilla nibh dolor, non porttitor nunc imperdiet et. Proin id mollis enim, sed efficitur justo.</p>
  <div class="card" style="left:710px;top:905px"><span role="img" aria-label="Illustration of half a gear joined to half a brain" style="background:radial-gradient(circle,#f5c042 0%,#e7775e 55%,#ffffff 100%)"></span></div>

  <div class="card" style="left:347px;top:1260px"><span role="img" aria-label="Illustration of a chip under a red roof" style="background:radial-gradient(circle,#3fa58a 0%,#e55a4f 55%,#ffffff 100%)"></span></div>
  <span class="num" style="left:647px;top:1270px">4.</span>
  <h3 class="benefit-head" style="left:647px;top:1330px">Praesent Iaculis Nunc</h3>
  <p class="benefit-text" style="left:647px;top:1369px">Duis fringilla nibh dolor, non porttitor nunc imperdiet et. Proin id mollis enim, sed efficitur justo.</p>
</section>

<footer class="signup">
  <div class="footer-brand"><span class="brand-dot"></span><span class="brand-name">Brightwell Loom</span></div>
  <div class="signup-form">
    <span class="signup-input">Enter Your Mail Id</span>
    <span class="signup-btn">
      <svg width="22" height="20" viewBox="0 0 22 20"><path d="M1 9 21 1 15 19 10 12Z" fill="#ffffff"/><path d="M10 12 21 1" stroke="#1fcf77" stroke-width="1.5"/></svg>
    </span>
  </div>
  <div class="social" aria-label="Social links">
    <span><i></i></span><span><i></i></span><span><i></i></span><span><i></i></span>
  </div>
</footer>

<div class="legal">© 2018 Brightwell Loom. All Rights Reserved | <b>Privacy Policy</b></div>

</body>
</html>
```